Business Card/Design Project for Personal Injury Lawyer

Personal Injury Attorney. I represent people who have been injured in accidents and are making money damage claims against the negligent party. As a personal injury attorney, I am a counselor, advisor, and legal representative to my clients. Clients want someone who is aggresssive yet professional.

More information about what I do an be found at www.vorlandlaw.example

Target Market(s)

General public.

Industry/Entity Type

Legal

Contact Information for Business Card

Need a new logo/brand image for b-cards, website, and letterhead/envelops. Looking for something original (no scales of justice or courthouse columns), yet classy and professional.

Here's what I'm thinking (but I'm always open to other ideas):

On the front, I would like my name (Colton R. Vorland), and underneath the words "Personal Injury Attorney." The background could be black, for example, and the lettering could be white or foil. I'm open to differnt colors, or even two colors. My name on the front side should pop.

And then on the back would be all my contact info, and maybe a logo or a slogan.

Here are two slogans I've come up with so far: 1. Settle for More. 2. Real Answers for People Hurt in Accidents.

Requirements
Must have
• Something that identifys me as a personal injury attorney, such as the words Personal Injury Attorney (or Lawyer, or Law Firm, etc.).
Nice to have
• A style/image that can be used nicely on my website and on letterhead.
Should not have
• Tired, commonly used logos or symbols, such a scales of justice or courthouse columns.

```html
<!DOCTYPE html>
<html lang="en">
<head>
<meta charset="utf-8">
<title>Vorland Law – Business Card</title>
<link rel="stylesheet" href="https://fonts.googleapis.com/css2?family=Cinzel:wght@400&family=Open+Sans:wght@400;600&display=swap">
<style>
  :root {
    --stage: #ebe8e5;
    --card-black: #050505;
    --brand-red: #ee0018;
    --white: #ffffff;
    --muted: #d8d8d8;
    --rule: #8a8a8a;
  }
  * { margin: 0; padding: 0; box-sizing: border-box; }
  html, body { width: 1200px; height: 900px; overflow: hidden; }
  body { background: var(--stage); position: relative; font-family: "Open Sans", sans-serif; }

  .card { position: absolute; border-radius: 14px; overflow: hidden; }
  .card-front { left: 78px; top: 34px; width: 588px; height: 364px; background: var(--card-black); }
  .card-back { left: 389px; top: 506px; width: 566px; height: 350px; background: var(--brand-red); }

  .band { position: absolute; }
  .card-front .band { top: 30px; height: 98px; background: var(--brand-red); }
  .card-front .band-left { left: 0; width: 237px; }
  .card-front .band-right { left: 367px; right: 0; }
  .card-back .band { top: 81px; height: 96px; background: var(--white); }
  .card-back .band-left { left: 0; width: 229px; }
  .card-back .band-right { left: 351px; right: 0; }

  .brand-square { position: absolute; border: 2px solid; }
  .card-front .brand-square { left: 255px; top: 32px; width: 94px; height: 120px; border-color: var(--brand-red); }
  .card-back .brand-square { left: 248px; top: 72px; width: 86px; height: 111px; border-color: var(--white); }

  .brand-name { position: absolute; text-align: center; font-family: "Cinzel", serif; font-weight: 400; letter-spacing: 1px; line-height: 1; }
  .card-front .brand-name { left: 178px; width: 232px; top: 163px; font-size: 36px; color: var(--brand-red); }
  .card-back .brand-name { left: 0; right: 0; top: 207px; font-size: 34px; color: var(--white); }

  .brand-sub { position: absolute; display: flex; align-items: center; gap: 6px; font-family: "Cinzel", serif; font-size: 12px; letter-spacing: 1px; }
  .brand-sub::before, .brand-sub::after { content: ""; flex: 1; height: 1px; background: currentColor; }
  .card-front .brand-sub { left: 178px; width: 232px; top: 204px; color: var(--rule); }
  .card-back .brand-sub { left: 177px; width: 212px; top: 243px; color: var(--white); }

  .person { position: absolute; left: 31px; top: 272px; }
  .person-name { font-size: 20px; font-weight: 600; color: var(--brand-red); line-height: 1.2; }
  .person-title { font-size: 16px; color: var(--muted); margin-top: 3px; }

  .contact { position: absolute; right: 36px; top: 243px; list-style: none; }
  .contact li { display: flex; justify-content: flex-end; align-items: center; gap: 8px; height: 24.5px; font-size: 15px; color: var(--muted); }
  .contact svg { width: 12px; height: 12px; fill: var(--brand-red); }

  .slogan { position: absolute; left: 0; right: 0; top: 280px; text-align: center; font-family: "Cinzel", serif; font-size: 18px; color: var(--white); letter-spacing: 0.5px; }
</style>
</head>
<body>

<section class="card card-front">
  <div class="band band-left"></div>
  <div class="band band-right"></div>
  <div class="brand-square"></div>
  <div class="brand-name">Vorland</div>
  <div class="brand-sub">Law</div>

  <div class="person">
    <p class="person-name">Colton R. Vorland</p>
    <p class="person-title">Personal Injury Attorney</p>
  </div>

  <ul class="contact">
    <li>(044)-456-7890
      <svg viewBox="0 0 12 12"><path d="M2.5 0.5l2 2.2-1.1 1.4a7 7 0 0 0 4.5 4.5l1.4-1.1 2.2 2-1.2 2C5 11.5 0.5 7 0.5 1.7z"/></svg>
    </li>
    <li>123-456-7890
      <svg viewBox="0 0 12 12"><path d="M3 1h6a1 1 0 0 1 1 1v9H2V2a1 1 0 0 1 1-1zm1 3v2h4V4z"/></svg>
    </li>
    <li>info@youremail.com
      <svg viewBox="0 0 12 12"><path d="M0 2h12v1L6 7 0 3zM0 4.2l6 4 6-4V10H0z"/></svg>
    </li>
    <li>www.website.com
      <svg viewBox="0 0 12 12"><circle cx="6" cy="6" r="5.5"/></svg>
    </li>
  </ul>
</section>

<section class="card card-back">
  <div class="band band-left"></div>
  <div class="band band-right"></div>
  <div class="brand-square"></div>
  <div class="brand-name">Vorland</div>
  <div class="brand-sub">Law</div>
  <p class="slogan">Real Answers for People Hurt in Accidents</p>
</section>

</body>
</html>
```